Diabetes Education Flyer Design Project

We need a 8.5" X 11" flyer design for a retail pharmacy located in Queens, NYC to promote our new program of "Free Diabetes Education". This flyer will be distributed to doctors offices and to places where people congregate. The flyer should create a fear to the audience about diabetes and an urgency to come or call the pharmacy to get more information on the "Free Diabetes Education". The target audience is 40+ years old with national background of West Indies and India. They are mostly blue color worker with a highschool or less education

Target Market(s)

People with diabetes aging 40+, from West Indies and India, low literacy level

Industry/Entity Type

Education

Requirements
Must have
• Must have graphics and colors to attract the targetted age/race/literacy. Must have graphics and colors to create fear at the begining and hope at the end.
Nice to have
• Fonts to support the theme

```html
<!DOCTYPE html>
<html lang="en">
<head>
<meta charset="utf-8">
<title>Diabetes Education Flyer</title>
<link rel="stylesheet" href="https://fonts.googleapis.com/css2?family=Poppins:wght@800&family=PT+Sans+Narrow:wght@400;700&family=PT+Sans:wght@700&display=swap">
<style>
  :root {
    --stage: #e9e9e9;
    --snow-light: #fbfcfd;
    --snow-mid: #eef1f4;
    --snow-shade: #dfe4ea;
    --title-grey: #9aa0a6;
    --title-edge: #6e747a;
    --gold: #d9a11a;
    --brand-red: #d21f26;
    --deep-red: #8c1c1f;
    --sugar: #cfd4d8;
    --sieve-shadow: #b7bcc1;
  }
  * { box-sizing: border-box; margin: 0; padding: 0; }
  html, body { width: 1200px; height: 900px; overflow: hidden; }
  body { background: var(--stage); position: relative; }

  .flyer {
    position: absolute; left: 268px; top: 20px;
    width: 664px; height: 860px; overflow: hidden;
    box-shadow: 0 4px 18px rgba(0,0,0,.18);
    font-family: "PT Sans Narrow", "Arial Narrow", sans-serif;
  }
  .snow-backdrop {
    position: absolute; inset: 0;
    background:
      radial-gradient(ellipse at 30% 40%, var(--snow-light) 0%, transparent 60%),
      radial-gradient(ellipse at 75% 70%, var(--snow-light) 0%, transparent 55%),
      linear-gradient(160deg, var(--snow-mid), var(--snow-shade) 55%, var(--snow-mid));
  }
  .headline {
    position: absolute; left: 0; right: 0; top: 8px;
    text-align: center;
    font-family: "Poppins", sans-serif; font-weight: 800;
    font-size: 128px; line-height: 1; letter-spacing: 2px;
    color: var(--title-grey);
    -webkit-text-stroke: 2px var(--title-edge);
  }
  .death-toll {
    position: absolute; left: 0; right: 0; top: 140px;
    text-align: center; color: var(--gold);
    font-family: "PT Sans", sans-serif; font-weight: 700; font-size: 30px;
  }
  .question {
    position: absolute; left: 0; right: 0; top: 172px;
    text-align: center; color: var(--gold);
    font-weight: 700; font-size: 66px; line-height: 0.95;
  }
  .question sup { font-size: 22px; vertical-align: 30px; }
  .brand {
    font-family: "PT Sans", sans-serif; font-weight: 700;
    color: var(--brand-red); text-transform: lowercase;
    display: flex; align-items: center; gap: 6px;
  }
  .brand-square { width: 12px; height: 12px; background: var(--brand-red); display: inline-block; }
  .brand--offer { position: absolute; left: 34px; top: 424px; font-size: 28px; }
  .offer-rule { position: absolute; left: 34px; right: 14px; top: 462px; height: 2px; background: var(--brand-red); }
  .offer-copy {
    position: absolute; right: 14px; top: 470px; width: 520px;
    text-align: right; color: var(--deep-red);
    font-weight: 700; font-size: 25px; line-height: 1.08;
  }
  .sugar-sieve {
    position: absolute; left: 14px; top: 548px; width: 270px; height: 230px;
    border-radius: 50% 50% 40% 40%;
    background: radial-gradient(circle at 45% 40%, var(--snow-light) 0%, var(--sugar) 55%, var(--sieve-shadow) 100%);
  }
  .contact { position: absolute; left: 380px; top: 652px; width: 260px; }
  .brand--contact { font-size: 34px; }
  .address { color: var(--deep-red); font-size: 19px; line-height: 1.15; margin-top: 8px; margin-left: 20px; }
  .phone { color: var(--deep-red); font-weight: 700; font-size: 28px; margin-top: 6px; margin-left: 20px; }
  .footnote {
    position: absolute; left: 14px; top: 786px; width: 340px;
    color: var(--gold); font-size: 11px; line-height: 1.2;
  }
</style>
</head>
<body>
  <main class="flyer">
    <div class="snow-backdrop" role="img" aria-label="Snowy white sugar texture with faint snowflake patterns"></div>

    <h1 class="headline">Diabetes</h1>
    <p class="death-toll">Kills 3,400,000 People</p>
    <p class="question">In a Year<sup>1</sup><br>Are You<br>the Next?</p>

    <div class="brand brand--offer"><span>qvb pharmacy</span><span class="brand-square"></span></div>
    <div class="offer-rule"></div>
    <p class="offer-copy">Is Offering FREE Education for Diabetics<br>Call or Stop by Now! Your Life Depends on It!<br>Educate Yourself and Live Longer</p>

    <div class="sugar-sieve" role="img" aria-label="Photo of a metal sieve full of white sugar"></div>

    <address class="contact" style="font-style:normal">
      <div class="brand brand--contact"><span>qvb pharmacy</span><span class="brand-square"></span></div>
      <p class="address">84-20 Maple Ave.,<br>Kew Gardens, NY 11415</p>
      <p class="phone">(718) 555-0172</p>
    </address>

    <p class="footnote"><sup>1</sup> Based on global health figures, an estimated 3.4 million people die each year from the effects of high blood sugar. Source: health report.</p>
  </main>
</body>
</html>
```